Ridgeline Outfitters Business Cards

Recently had a logo done with Artfolio and now looking for a business card to go along with it.

Target Market(s)

Ridgeline Outfitters is a weapons dealer. My market will be primarily men, hunting, shooting type.

Industry/Entity Type

Business

Contact Information for Business Card

I selected double sided, but this is not required, single or double is going to be fine. I picture the logo on one side, or perhaps just the circle which contains "RO" with the remaining info on the other side.

Font styles to use
Sans Serif

Requirements
Must have
• My name: Milo Brandt
• Title: Owner
• tel: 612-555-0187
• web: www.ridgelineoutfittersmn.example
Nice to have
• I like the concept of a black business card. I would like to keep the colors monotone, black, grey, white or red. Red is acceptable because it is in the logo. I have also seen cards that are matte black with shiny black as well, perhaps for the logo (or circle RO) part of the logo.
• I will upload a couple of the logos for use, and also an example I just found of the black on black. and some others that have a nice contrast.
Should not have
• lots of colors are not wanted.

```html
<!DOCTYPE html>
<html lang="en">
<head>
<meta charset="utf-8">
<title>Ridgeline Outfitters Business Card</title>
<link rel="stylesheet" href="https://fonts.googleapis.com/css2?family=Lato:wght@400;700;900&display=swap">
<style>
  :root {
    --stage: #e4e1dc;
    --card-black: #1e1e1f;
    --card-dark: #262627;
    --panel-grey: #3b3b3d;
    --divider: #0c0c0c;
    --brand-red: #e0343a;
    --steel: #8d8e91;
    --text-light: #d6d6d6;
    --icon-bg: #0f0f10;
  }
  * { margin: 0; padding: 0; box-sizing: border-box; }
  html, body { width: 1200px; height: 675px; overflow: hidden; }
  body {
    background: var(--stage);
    font-family: "Lato", sans-serif;
    position: relative;
  }
  .card {
    position: absolute;
    top: 188px;
    width: 520px;
    height: 298px;
    border-radius: 4px;
    overflow: hidden;
    box-shadow: 0 10px 24px rgba(0,0,0,.28);
    background:
      radial-gradient(circle, rgba(255,255,255,.05) 1px, transparent 1.4px) 0 0 / 5px 5px,
      var(--card-black);
  }
  .card--back { left: 50px; }
  .card--front { left: 630px; }

  .back-shape { position: absolute; inset: 0; }

  .brand {
    position: absolute;
    display: flex;
    align-items: center;
    gap: 14px;
  }
  .brand__mark {
    width: 54px; height: 54px;
    border-radius: 50%;
    border: 4px solid var(--steel);
    flex: none;
  }
  .brand__name {
    color: var(--brand-red);
    font-weight: 900;
    text-transform: uppercase;
    letter-spacing: 1px;
    line-height: 1.05;
    font-size: 24px;
  }
  .card--front .brand { left: 86px; top: 116px; }
  .card--back .brand { left: 28px; top: 118px; flex-direction: column; align-items: flex-start; gap: 16px; }
  .card--back .brand__name { font-size: 19px; }
  .card--back .brand__mark { width: 70px; height: 70px; margin-left: 36px; }

  .contact {
    position: absolute;
    left: 276px;
    right: 12px;
    top: 52px;
    list-style: none;
    color: var(--text-light);
    font-size: 10.5px;
    line-height: 1.35;
  }
  .contact__item { display: flex; align-items: center; gap: 12px; margin-bottom: 26px; }
  .contact__strong { font-weight: 700; color: #f0f0f0; }
  .contact__icon {
    width: 26px; height: 26px; border-radius: 50%;
    background: var(--icon-bg);
    display: flex; align-items: center; justify-content: center;
    flex: none;
  }
  .contact__icon svg { width: 14px; height: 14px; fill: var(--text-light); }
</style>
</head>
<body>

<section class="card card--back" aria-label="Card back">
  <svg class="back-shape" viewBox="0 0 520 298" preserveAspectRatio="none" aria-hidden="true">
    <path d="M265 0 C 225 90, 225 200, 265 298 L520 298 L520 0 Z" fill="var(--panel-grey)"/>
    <path d="M250 0 C 210 90, 210 200, 250 298 L265 298 C 225 200, 225 90, 265 0 Z" fill="var(--divider)"/>
    <path d="M0 0 L250 0 C 238 28, 230 50, 224 70 L0 70 Z" fill="var(--card-dark)" opacity=".6"/>
  </svg>

  <div class="brand">
    <span class="brand__name">Ridgeline<br>Outfitters</span>
    <span class="brand__mark"></span>
  </div>

  <ul class="contact">
    <li class="contact__item">
      <span class="contact__icon"><svg viewBox="0 0 24 24"><path d="M6.6 10.8a15.1 15.1 0 0 0 6.6 6.6l2.2-2.2a1 1 0 0 1 1-.25 11.4 11.4 0 0 0 3.6.57 1 1 0 0 1 1 1V20a1 1 0 0 1-1 1A17 17 0 0 1 3 4a1 1 0 0 1 1-1h3.5a1 1 0 0 1 1 1c0 1.25.2 2.45.57 3.57a1 1 0 0 1-.25 1z"/></svg></span>
      <span><span class="contact__strong">Milo Brandt</span> · Owner<br>612-555-0187</span>
    </li>
    <li class="contact__item">
      <span class="contact__icon"><svg viewBox="0 0 24 24"><path d="M3 5h18v14H3zm2 2v.5l7 4.5 7-4.5V7zm0 3v7h14v-7l-7 4.5z"/></svg></span>
      <span>milo@ridgelineoutfittersmn.example<br>www.ridgelineoutfittersmn.example</span>
    </li>
    <li class="contact__item">
      <span class="contact__icon"><svg viewBox="0 0 24 24"><path d="M12 2a7 7 0 0 0-7 7c0 5 7 13 7 13s7-8 7-13a7 7 0 0 0-7-7zm0 9.5A2.5 2.5 0 1 1 12 6.5a2.5 2.5 0 0 1 0 5z"/></svg></span>
      <span>Your Street name, City,<br>Country, Zip Code.</span>
    </li>
  </ul>
</section>

<section class="card card--front" aria-label="Card front">
  <div class="brand">
    <span class="brand__mark"></span>
    <span class="brand__name">Ridgeline Outfitters</span>
  </div>
</section>

</body>
</html>
```